Lantern CD Jacket - BSC Worship Album

Album Name: Lantern | Artist: BSC Worship

We need a CD Jacket with these items:
1. Front Cover design to be displayed on Sonora, Playvio, etc.
2. Back Cover design with song titles and production info
3. Insert Sheet design containing All Lyrics and Credit Title
4. CD Plate design

The final design should communicate a commitment to be like our Lord Jesus Christ in an abstract / subtle way.

Lantern meaning: Two or more subjects similar to each other.

This is the theme song lyrics to summarized the meaning:
LANTERN // Great is the Lord God almighty / Your Kingdom come, Your will be done // Great is the Lord God almighty / You saved my life, You give me hope // And through it all / With all I am // Lantern... I will shine like You Jesus / Your love and Your grace live in me / Lantern... I will live like You Jesus / Through all I will be… Lantern

--------------------------------------------------

TRACKS:
1. Lantern
2. Sungai Pagi
3. Lembah Sunyi
4. Pelita
5. Jalan Berliku
6. Fajar
7. Gunung Batu Tinggi
8. Angin Selatan
9. Rumah Kayu
10. Open Skies

Produced & arranged by Andreas Wibisono
© 2017 BSC Worship

Attached files:
1. All Lyrics and Credit Title on PDF and TXT format
2. “Lantern” theme song on MP3 format for your reference
3. BSC Logo (use the round ones). Do not put the logo on the front cover. Use it to incorporate the production info at the back cover only
Updates

Reason: Only received 14 designs. Not so many choices as advertised.

Target Market(s)

Sonora & Playvio Subscribers

Colors

Designer to choose colors to be used in the design.

Requirements
Must have
• Great & eye catching design
Nice to have
• Lantern meaning: Two or more subjects similar to each other
Should not have
• Non-Christian values

```html
<!DOCTYPE html>
<html lang="en">
<head>
<meta charset="utf-8">
<title>Lantern CD Jacket – BSC Worship</title>
<link rel="stylesheet" href="https://fonts.googleapis.com/css2?family=Josefin+Sans:wght@300;400;600&display=swap">
<style>
  :root {
    --stage: #e4e4e7;
    --gold: #c9a548;
    --gold-light: #dcbf6e;
    --teal-deep: #137f98;
    --teal-mid: #2fa9bb;
    --teal-light: #8fdde0;
    --mist: #cdeeed;
    --paper: #fbfbf8;
    --rim: #3a3d42;
    --hub: #55585e;
  }
  * { margin: 0; padding: 0; box-sizing: border-box; }
  html, body { width: 1200px; height: 1000px; overflow: hidden; }
  body {
    background: var(--stage);
    font-family: "Josefin Sans", sans-serif;
    position: relative;
  }

  .panel { position: absolute; }

  /* Back cover */
  .back-cover { left: 60px; top: 75px; width: 385px; height: 375px; }
  .back-cover .artwork, .front-cover .artwork {
    position: absolute; inset: 0;
    border: 7px solid var(--gold);
  }
  .back-cover .artwork {
    background: radial-gradient(circle at 70% 85%, var(--teal-light) 0%, var(--teal-mid) 35%, var(--teal-deep) 80%);
  }
  .back-cover .corner-name {
    position: absolute; left: 26px; top: 36px;
    color: var(--gold); font-size: 10px; letter-spacing: 2px; font-weight: 400;
  }
  .track-list {
    position: absolute; left: 60px; right: 30px; top: 68px;
    list-style: none; text-align: center;
    color: #ffffff; font-size: 13px; letter-spacing: 1.4px; line-height: 18px;
    font-weight: 400; text-transform: uppercase;
  }
  .track-list .num { color: var(--gold-light); }
  .production-info {
    position: absolute; left: 60px; right: 30px; top: 264px;
    text-align: center; color: var(--gold-light);
    font-size: 9px; letter-spacing: 1.1px; line-height: 12px; text-transform: uppercase;
  }
  .church-badge {
    position: absolute; right: 18px; bottom: 20px;
    display: flex; align-items: center; gap: 4px;
  }
  .church-badge .dot { width: 12px; height: 12px; border-radius: 50%; background: #ffffff; }
  .church-badge .name { color: #ffffff; font-size: 12px; font-weight: 600; letter-spacing: 1px; }

  /* Front cover */
  .front-cover { left: 485px; top: 75px; width: 390px; height: 375px; }
  .front-cover .artwork {
    background: linear-gradient(170deg, var(--mist) 0%, var(--teal-light) 45%, var(--teal-mid) 100%);
  }
  .front-cover .album-title {
    position: absolute; left: 0; right: 0; top: 174px; text-align: center;
    color: var(--gold); font-size: 20px; letter-spacing: 5px; font-weight: 400;
  }
  .front-cover .artist {
    position: absolute; left: 0; right: 0; top: 316px; text-align: center;
    color: #ffffff; font-size: 11px; letter-spacing: 3px; font-weight: 400;
  }

  /* CD plate */
  .cd-plate { left: 805px; top: 85px; width: 360px; height: 360px; }
  .cd-plate svg { position: absolute; inset: 0; }
  .cd-plate .disc-title {
    position: absolute; left: 20px; width: 120px; top: 168px; text-align: center;
    color: var(--gold); font-size: 11px; letter-spacing: 2px;
  }
  .cd-plate .disc-artist {
    position: absolute; left: 20px; width: 120px; top: 225px; text-align: center;
    color: #ffffff; font-size: 8px; letter-spacing: 1.6px;
  }
  .cd-plate .disc-tracks {
    position: absolute; left: 215px; top: 146px; list-style: none; text-align: center;
    color: #ffffff; font-size: 8.6px; line-height: 11.6px; letter-spacing: .8px; text-transform: uppercase;
  }
  .cd-plate .disc-tracks .num { color: var(--gold-light); }
  .arc-text { fill: var(--gold); font-size: 7.5px; letter-spacing: 1px; font-family: "Josefin Sans", sans-serif; }

  /* Insert sheet */
  .insert-sheet {
    left: 260px; top: 560px; width: 680px; height: 340px;
    display: flex; background: var(--gold); padding: 6px;
  }
  .insert-page {
    flex: 1; background: var(--paper); display: flex; gap: 18px;
    padding: 22px 20px;
  }
  .insert-page + .insert-page { border-left: 1px solid #e0ded6; }
  .lyric-column { flex: 1; }
  .song-block { margin-bottom: 18px; }
  .song-block h3 {
    color: var(--gold); font-size: 7.5px; font-weight: 600; letter-spacing: .8px; margin-bottom: 3px;
  }
  .song-block p { color: var(--gold); font-size: 7px; line-height: 10.5px; font-weight: 300; }
  .song-block .credit { opacity: .8; margin-bottom: 4px; }
</style>
</head>
<body>

  <!-- Back cover -->
  <section class="panel back-cover">
    <div class="artwork" role="img" aria-label="Soft teal bokeh light background"></div>
    <span class="corner-name">LANTERN</span>
    <ol class="track-list">
      <li><span class="num">1.</span> Lantern</li>
      <li><span class="num">2.</span> Sungai Pagi</li>
      <li><span class="num">3.</span> Lembah Sunyi</li>
      <li><span class="num">4.</span> Pelita</li>
      <li><span class="num">5.</span> Jalan Berliku</li>
      <li><span class="num">6.</span> Fajar</li>
      <li><span class="num">7.</span> Gunung Batu Tinggi</li>
      <li><span class="num">8.</span> Angin Selatan</li>
      <li><span class="num">9.</span> Rumah Kayu</li>
      <li><span class="num">10.</span> Open Skies</li>
    </ol>
    <p class="production-info">Produced &amp; arranged by Andreas Wibisono<br>© 2017 BSC Worship</p>
    <div class="church-badge"><span class="dot"></span><span class="name">BSC</span></div>
  </section>

  <!-- Front cover -->
  <section class="panel front-cover">
    <div class="artwork" role="img" aria-label="Pale aqua bokeh light background"></div>
    <span class="album-title">LANTERN</span>
    <span class="artist">BSC WORSHIP</span>
  </section>

  <!-- CD plate -->
  <section class="panel cd-plate">
    <svg viewBox="0 0 360 360">
      <defs>
        <linearGradient id="disc-fill" x1="0" y1="0" x2="0.3" y2="1">
          <stop offset="0" stop-color="#d2f0ee"/>
          <stop offset="0.5" stop-color="#8fdde0"/>
          <stop offset="1" stop-color="#3fb2c2"/>
        </linearGradient>
        <path id="arc-top" d="M 40,180 A 140,140 0 0 1 320,180"/>
      </defs>
      <circle cx="180" cy="180" r="179" fill="var(--rim)"/>
      <circle cx="180" cy="180" r="172" fill="url(#disc-fill)" role="img" aria-label="Aqua bokeh light disc artwork"/>
      <circle cx="180" cy="180" r="170" fill="none" stroke="var(--gold)" stroke-width="3"/>
      <circle cx="180" cy="180" r="46" fill="none" stroke="#ffffff" stroke-opacity=".6" stroke-width="1"/>
      <circle cx="180" cy="180" r="24" fill="var(--hub)"/>
      <circle cx="180" cy="180" r="17" fill="#2c2e33"/>
      <text class="arc-text"><textPath href="#arc-top" startOffset="8%">PRODUCED &amp; ARRANGED BY ANDREAS WIBISONO</textPath></text>
      <text class="arc-text"><textPath href="#arc-top" startOffset="69%">© 2017 BSC WORSHIP</textPath></text>
    </svg>
    <span class="disc-title">LANTERN</span>
    <span class="disc-artist">BSC WORSHIP</span>
    <ol class="disc-tracks">
      <li><span class="num">1.</span> Lantern</li>
      <li><span class="num">2.</span> Sungai Pagi</li>
      <li><span class="num">3.</span> Lembah Sunyi</li>
      <li><span class="num">4.</span> Pelita</li>
      <li><span class="num">5.</span> Jalan Berliku</li>
      <li><span class="num">6.</span> Fajar</li>
      <li><span class="num">7.</span> Gunung Batu Tinggi</li>
      <li><span class="num">8.</span> Angin Selatan</li>
      <li><span class="num">9.</span> Rumah Kayu</li>
      <li><span class="num">10.</span> Open Skies</li>
    </ol>
  </section>

  <!-- Insert sheet -->
  <section class="panel insert-sheet">
    <div class="insert-page">
      <div class="lyric-column">
        <article class="song-block">
          <h3>01. LANTERN</h3>
          <p class="credit">Words &amp; music by the worship team</p>
          <p>Great is the Lord our God<br>Your kingdom come in us<br>And through it all we sing<br>Lantern, I will shine</p>
        </article>
        <article class="song-block">
          <h3>02. SUNGAI PAGI</h3>
          <p class="credit">Words &amp; music by the worship team</p>
          <p>Morning light is on the river<br>Grace that flows from You</p>
        </article>
      </div>
      <div class="lyric-column">
        <article class="song-block">
          <h3>03. LEMBAH SUNYI</h3>
          <p>In the quiet valley You are near<br>Every step I take is Yours<br>Hold me close, my Lord</p>
        </article>
        <article class="song-block">
          <h3>04. PELITA</h3>
          <p>A small light in the dark<br>Burning bright for all to see</p>
        </article>
      </div>
    </div>
    <div class="insert-page">
      <div class="lyric-column">
        <article class="song-block">
          <h3>05. JALAN BERLIKU</h3>
          <p>Winding roads still lead to You<br>Faithful hands will guide me home</p>
        </article>
        <article class="song-block">
          <h3>06. FAJAR</h3>
          <p>Dawn is breaking on the hills<br>New mercy every day</p>
        </article>
      </div>
      <div class="lyric-column">
        <article class="song-block">
          <h3>07. GUNUNG BATU TINGGI</h3>
          <p>You are my rock and refuge<br>Strong tower, steady ground</p>
        </article>
        <article class="song-block">
          <h3>08. ANGIN SELATAN</h3>
          <p>Wind of the Spirit, move in me<br>Blow through every open door</p>
        </article>
      </div>
    </div>
  </section>

</body>
</html>
```